BUILDERS MERCHANTS BUSINESS CARD

we need a business card for our long established builders merchants
we supply to both trade and diy
we offer an express delivery service
we would like TRV to standout as this our main trade mark logo
also our main colours are blue/white/yellow

Industry/Entity Type

Trade

Contact Information for Business Card

TRV BUILDERS MERCHANTS

SUPPLIERS OF ALL TYPES OF BUILDING MATERIALS

-SAND/CEMENT
-BRICKS/BLOCKS
-PLASTER/PLASTERBOARDS
-INSULATION
-FENCING/GARDEN PAVING
-PLUMBING
-ELECTRICAL
-EXPRESS DELIVERIES

EST OVER 30 YEARS

418 MARLOWE RISE
LONDON
NORWOOD
SE19 4XD

0208 5294861
0208 5392617
FAX 0208539 7283
EMAIL- TRVBUILDERSMERCHANTS@POSTVALE.CO.UK

```html
<!DOCTYPE html>
<html lang="en">
<head>
<meta charset="utf-8">
<title>TRV Builders Merchants – Business Card</title>
<link href="https://fonts.googleapis.com/css2?family=Roboto+Condensed:wght@400;700&display=swap" rel="stylesheet">
<style>
  :root {
    --backdrop: #3a3a3a;
    --card: #1d1d1e;
    --text: #f2f2f2;
    --blue: #1f6fb8;
    --white: #ececec;
    --yellow: #e8e000;
  }
  * { margin: 0; padding: 0; box-sizing: border-box; }
  html, body {
    width: 1200px; height: 900px; overflow: hidden;
    background: var(--backdrop);
  }
  .canvas {
    width: 1200px; height: 900px;
    display: flex; align-items: center; justify-content: center;
  }
  .card {
    position: relative; width: 540px; height: 840px;
    padding: 44px 40px 34px;
    background: var(--card);
    color: var(--text);
    font-family: "Roboto Condensed", "Arial Narrow", sans-serif;
    box-shadow: 0 10px 30px rgba(0,0,0,.45);
    display: flex; flex-direction: column;
    white-space: nowrap;
  }
  .brand { display: flex; align-items: center; gap: 14px; }
  .brand-name {
    font-weight: 700; font-size: 100px; line-height: 1;
    letter-spacing: 2px; color: var(--white);
  }
  .brand-mark { width: 22px; height: 22px; background: var(--yellow); }

  .tricolour { height: 6px; display: flex; flex: none; }
  .tricolour span { flex: 1; }
  .tricolour .blue { background: var(--blue); }
  .tricolour .white { background: var(--white); }
  .tricolour .yellow { background: var(--yellow); }
  .bar-brand { width: 260px; margin-top: 14px; }
  .bar-services { width: 300px; margin: 26px auto 0; }
  .bar-contact { width: 300px; margin: 34px 0 0 auto; }

  .services {
    margin-top: 26px;
    text-align: center; font-size: 20px; line-height: 27px;
  }
  .contacts {
    list-style: none; font-size: 20px; line-height: 31px;
    margin: 30px 0 0 130px;
  }
  .contacts li, .email { display: flex; align-items: center; gap: 10px; }
  .icon { width: 18px; height: 18px; flex: none; }
  .email { margin-top: 44px; font-size: 20px; }

  .brand-small { margin: 22px 20px 0 auto; gap: 8px; }
  .brand-small .brand-name { font-size: 46px; }
  .brand-small .brand-mark { width: 10px; height: 10px; }

  .address {
    margin-top: auto;
    text-align: center; font-size: 21px; letter-spacing: .3px;
  }
</style>
</head>
<body>
<main class="canvas">
  <article class="card">
    <div class="brand">
      <span class="brand-name">TRV</span>
      <span class="brand-mark"></span>
    </div>
    <div class="tricolour bar-brand"><span class="blue"></span><span class="white"></span><span class="yellow"></span></div>

    <p class="services">
      BUILDERS MERCHANTS SUPPLIERS OF ALL<br>
      TYPES OF BUILDING MATERIALS -SAND/CEMENT<br>
      -BRICKS/BLOCKS -PLASTER/PLASTERBOARDS<br>
      -INSULATION -FENCING/GARDEN PAVING<br>
      -PLUMBING -ELECTRICAL -EXPRESS DELIVERIES<br>
      EST OVER 30 YEARS
    </p>

    <div class="tricolour bar-services"><span class="blue"></span><span class="white"></span><span class="yellow"></span></div>

    <ul class="contacts">
      <li>
        <svg class="icon" viewBox="0 0 18 18" aria-hidden="true">
          <rect x="1" y="1" width="16" height="16" rx="2" fill="none" stroke="#e8e000" stroke-width="2"/>
          <path d="M5 5c0 5 3 8 8 8l1-2-2-1-1 1c-2-1-3-2-4-4l1-1-1-2z" fill="#e8e000"/>
        </svg>
        0208 5294861
      </li>
      <li>
        <svg class="icon" viewBox="0 0 18 18" aria-hidden="true">
          <rect x="1" y="1" width="16" height="16" rx="2" fill="none" stroke="#e8e000" stroke-width="2"/>
          <rect x="6" y="4" width="6" height="10" rx="1" fill="none" stroke="#e8e000" stroke-width="1.5"/>
        </svg>
        0208 5392617
      </li>
      <li>
        <svg class="icon" viewBox="0 0 18 18" aria-hidden="true">
          <rect x="1" y="1" width="16" height="16" rx="2" fill="none" stroke="#e8e000" stroke-width="2"/>
          <rect x="4" y="8" width="10" height="6" fill="#e8e000"/>
          <rect x="6" y="4" width="6" height="4" fill="none" stroke="#e8e000" stroke-width="1.5"/>
        </svg>
        0208539 7283
      </li>
    </ul>

    <p class="email">
      <svg class="icon" viewBox="0 0 18 18" aria-hidden="true">
        <rect x="1" y="1" width="16" height="16" rx="2" fill="none" stroke="#e8e000" stroke-width="2"/>
        <path d="M4 5h10v8H4z M4 5l5 4 5-4" fill="none" stroke="#e8e000" stroke-width="1.5"/>
      </svg>
      TRVBUILDERSMERCHANTS@POSTVALE.CO.UK
    </p>

    <div class="tricolour bar-contact"><span class="blue"></span><span class="white"></span><span class="yellow"></span></div>

    <div class="brand brand-small">
      <span class="brand-name">TRV</span>
      <span class="brand-mark"></span>
    </div>

    <p class="address">418 MARLOWE RISE LONDON NORWOOD SE19 4XD</p>
  </article>
</main>
</body>
</html>
```